Cannabis company needs an e-commerce website

Our retail cannabis company Harbor Velvet needs a fully functioning e-commerce website optimized for SEO. We want the website to have the appeal and sophistication of a cigar lounge/boutique coffee shop highlighting our high-end artisanal products. It should have the ability to categorize and search for products based on tags. Our initial number of SKUs will be about 25, but that will grow as the business grows.

Target Market(s)

Online retail cannabis users

Industry/Entity Type

Cannabis

Coding

Coded - Design and coding required

Number of Pages Required

5+ page

Font styles to use
Sans Serif

Requirements
Must have
• - Age confirmation (19+) confirmation popup
- Very simple and easy method of purchasing based on different product sizes
- Search functionality based on tags etc. of the products
- Similar functionality to the following websites:
1) https://www.pinemarshleafco.com/
2) https://amberguild.io/
3) https://florivexa.org/
4) https://sagetrellis.com/
- Similar look to the following websites:
1) https://layoutgrove.net/item/dorvik-snuff-store-theme/48203716
2) https://www.stemcrest.ca/
3) https://northdunemade.org/
4) https://wellbrookflorals.com/

```html
<!DOCTYPE html>
<html lang="en">
<head>
<meta charset="utf-8">
<title>Harbor Velvet – Blog Details</title>
<link href="https://fonts.googleapis.com/css2?family=Lato:wght@400;700;900&display=swap" rel="stylesheet">
<style>
:root{
  --bg:#2c2c2c;
  --bg-dark:#232323;
  --bg-top:#262626;
  --line:#404040;
  --text:#d9d9d9;
  --muted:#bdbdbd;
  --white:#ffffff;
  --field:#2a2a2a;
  --field-line:#474747;
}
*{box-sizing:border-box;margin:0;padding:0}
html,body{width:1200px;height:2983px;overflow:hidden}
body{background:var(--bg);color:var(--text);font-family:'Lato',sans-serif;font-size:10.5px;line-height:1.8;position:relative}
.wrap{width:1028px;margin:0 auto;position:relative}
svg{display:block}

.topbar{height:30px;background:var(--bg-top);font-size:10.5px;color:var(--white)}
.topbar .wrap{display:flex;align-items:center;height:30px;justify-content:space-between}
.topbar .left,.topbar .right{display:flex;gap:22px;align-items:center}
.topbar span{display:flex;align-items:center;gap:6px}
.topbar .right span{color:var(--muted)}
.topbar .right span.acct{color:var(--white)}

.header{background:var(--bg-top);height:165px}
.header .brandrow{height:117px;display:flex;align-items:center;justify-content:space-between;border-bottom:1px solid var(--line)}
.brand{font-weight:900;font-size:25px;color:var(--white);letter-spacing:1px;text-transform:uppercase;line-height:1;text-align:center}
.tools{display:flex;gap:16px}
.nav{display:flex;justify-content:center;gap:34px;height:48px;align-items:center;font-size:12.5px;letter-spacing:.6px;color:var(--white);text-transform:uppercase}
.nav a{display:flex;align-items:center;gap:8px;color:inherit;text-decoration:none}

.crumbs{height:78px;background:var(--bg-dark)}
.crumbs .wrap{height:78px;display:flex;align-items:center;justify-content:space-between;font-weight:700;color:var(--white);font-size:11.5px;text-transform:uppercase}
.crumbs ol{list-style:none;display:flex;gap:6px;font-size:10.5px}
.crumbs ol li+li::before{content:"/";color:#888;margin-right:6px;font-weight:400}

.post{padding-top:53px}
.hero{height:289px;background:linear-gradient(120deg,#1d2130 0%,#283a22 40%,#4f8a22 65%,#2f5a1a 100%)}
.post h1{font-size:19.5px;font-weight:700;color:var(--white);text-transform:uppercase;margin-top:30px;letter-spacing:.2px}
.meta{display:flex;gap:24px;font-size:10.5px;color:var(--text);margin-top:12px}
.meta span{display:flex;gap:4px;align-items:center}
.body p{margin-top:14px;line-height:1.78}
.body p:first-child{margin-top:22px}
.gallery{display:flex;justify-content:space-between;margin-top:16px}
.gallery div{width:502px;height:301px}
.g-leaf{background:radial-gradient(circle at 50% 45%,#2f8a22 0%,#4aa82e 25%,#b5f08e 55%)}
.g-buds{background:linear-gradient(115deg,#f48a3a 0%,#9aa49a 25%,#7f9a5c 55%,#6f8f4a 80%,#4d7a2c 100%)}
.columns{display:flex;justify-content:space-between;margin-top:20px}
.columns ol{width:502px;list-style:none;font-weight:700;font-size:11px;color:var(--white);line-height:1}
.columns ol li{margin-bottom:16.5px}
.columns ol li:first-child{margin-top:8px}
.columns .text{width:502px}
.columns .text p{margin-bottom:12px;line-height:1.78}

.comments{margin-top:43px;border-top:1px solid var(--line)}
.comment{display:flex;gap:15px;height:169px;border-bottom:1px solid var(--line);padding-top:44px}
.avatar{width:49px;height:49px;border-radius:50%;flex:none;background:radial-gradient(circle,#e8d2c0,#b38b6d)}
.comment h4{font-size:10.5px;font-weight:700;color:var(--white);text-transform:uppercase;line-height:1.4}
.comment h4 small{font-weight:400;color:var(--muted);margin-left:14px;text-transform:none}
.comment p{margin-top:4px;line-height:1.78}

.leave{padding-top:48px}
.leave h2{font-size:29px;font-weight:700;color:var(--white);text-transform:uppercase;line-height:1}
.field{margin-top:17px}
.field label{display:block;font-weight:700;color:var(--white);font-size:11.5px;margin-bottom:4px}
.field .box{height:43px;border:1px solid var(--field-line);background:var(--field);padding:0 19px;display:flex;align-items:center;color:#8a8a8a;font-size:10px}
.field .box.area{height:122px;align-items:flex-start;padding-top:12px}
.btn{margin-top:22px;display:inline-block;width:135px;height:36px;border:1px solid var(--white);color:var(--white);font-weight:700;font-size:10.5px;line-height:34px;text-align:center;text-transform:uppercase}

.footer{position:absolute;top:2650px;left:0;width:1200px;height:333px;background:var(--bg-dark)}
.footer .cols{display:flex;height:278px;align-items:flex-start;padding-top:52px}
.fcol{text-align:center;color:var(--white);font-size:11px;line-height:2.2}
.fcol.about{width:262px;padding:8px 10px 0}
.fcol.about .brand{font-size:22px;margin-bottom:14px}
.divider{width:1px;height:147px;background:var(--line)}
.fcol.news{width:502px}
.fcol.news h3{font-size:27px;font-weight:700;text-transform:uppercase;line-height:1;margin-top:8px}
.fcol.news .email{margin:24px auto 0;width:336px;height:38px;border:1px solid var(--field-line);color:#8a8a8a;letter-spacing:3px;font-size:9px;line-height:36px}
.fcol.news .sub{margin:8px auto 0;width:105px;height:36px;border:1px solid var(--white);font-weight:700;font-size:10.5px;line-height:34px}
.fcol.store{width:263px;line-height:2.1}
.fcol.store h3{font-size:14px;font-weight:700;text-transform:uppercase;margin-bottom:8px}
.bottom{border-top:1px solid var(--line);height:55px}
.bottom .wrap{height:55px;display:flex;align-items:center;justify-content:space-between;color:var(--white);font-size:11px}
.cards{display:flex;gap:13px}
.cards i{width:20px;height:20px;border-radius:50%;background:#e8e8e8;display:block}
</style>
</head>
<body>

<div class="topbar">
  <div class="wrap">
    <div class="left">
      <span>Welcome to Our store Harbor Velvet</span>
      <span><svg width="10" height="10" viewBox="0 0 24 24"><path fill="#bbb" d="M6.6 10.8a15 15 0 006.6 6.6l2.2-2.2c.3-.3.7-.4 1-.2 1.1.4 2.3.6 3.6.6.6 0 1 .4 1 1V20c0 .6-.4 1-1 1A17 17 0 013 4c0-.6.4-1 1-1h3.5c.6 0 1 .4 1 1 0 1.3.2 2.5.6 3.6.1.3 0 .7-.2 1z"/></svg>Call Us: 555 - 018 - 2746</span>
    </div>
    <div class="right">
      <span><svg width="11" height="10" viewBox="0 0 24 22"><path fill="#fff" d="M12 21l-1.5-1.3C5 15 2 12.1 2 8.5 2 5.4 4.4 3 7.5 3c1.7 0 3.4.8 4.5 2.1C13.1 3.8 14.8 3 16.5 3 19.6 3 22 5.4 22 8.5c0 3.6-3 6.5-8.5 11.2z"/></svg>Wishlist</span>
      <span class="acct"><svg width="9" height="10" viewBox="0 0 20 22"><circle cx="10" cy="6" r="5" fill="#fff"/><path fill="#fff" d="M0 22c0-6 4.5-9 10-9s10 3 10 9z"/></svg>My Account <svg width="8" height="6" viewBox="0 0 8 6"><path d="M1 1l3 3 3-3" stroke="#fff" fill="none" stroke-width="1.3"/></svg></span>
    </div>
  </div>
</div>

<header class="header">
  <div class="wrap">
    <div class="brandrow">
      <svg width="19" height="16" viewBox="0 0 19 16"><rect y="0" width="19" height="3" fill="#fff"/><rect y="6.5" width="19" height="3" fill="#fff"/><rect y="13" width="19" height="3" fill="#fff"/></svg>
      <div class="brand">Harbor Velvet</div>
      <div class="tools">
        <svg width="19" height="19" viewBox="0 0 20 20"><circle cx="8" cy="8" r="6.5" stroke="#fff" stroke-width="1.6" fill="none"/><path d="M13 13l6 6" stroke="#fff" stroke-width="1.8"/></svg>
        <svg width="19" height="19" viewBox="0 0 20 20"><circle cx="10" cy="10" r="3" stroke="#fff" stroke-width="1.5" fill="none"/><circle cx="10" cy="10" r="7.5" stroke="#fff" stroke-width="1.5" fill="none" stroke-dasharray="3 1.6"/></svg>
        <svg width="19" height="19" viewBox="0 0 20 20"><path d="M2 7h16l-2 11H4z" stroke="#fff" stroke-width="1.5" fill="none"/><path d="M6 7l4-5 4 5M7 10v5M10 10v5M13 10v5" stroke="#fff" stroke-width="1.3" fill="none"/></svg>
      </div>
    </div>
    <nav class="nav">
      <a>Home</a>
      <a>Shop <svg width="9" height="6" viewBox="0 0 9 6"><path d="M1 1l3.5 3.5L8 1" stroke="#fff" fill="none" stroke-width="1.5"/></svg></a>
      <a>About</a>
      <a>Product <svg width="9" height="6" viewBox="0 0 9 6"><path d="M1 1l3.5 3.5L8 1" stroke="#fff" fill="none" stroke-width="1.5"/></svg></a>
      <a>Brands <svg width="9" height="6" viewBox="0 0 9 6"><path d="M1 1l3.5 3.5L8 1" stroke="#fff" fill="none" stroke-width="1.5"/></svg></a>
      <a>Blog</a>
      <a>FAQ</a>
    </nav>
  </div>
</header>

<section class="crumbs">
  <div class="wrap">
    <span>Blog Details</span>
    <ol><li>Home</li><li>Blog</li><li>Blog Deatils</li></ol>
  </div>
</section>

<main class="wrap post">
  <div class="hero" role="img" aria-label="Close-up photo of green cannabis leaves against a dark background"></div>
  <h1>Also the leap into electronic typesetting, remaining essentially unchanged.</h1>
  <div class="meta">
    <span>25 January 2018</span>
    <span>Posted By : Admin</span>
    <span><svg width="11" height="10" viewBox="0 0 24 22"><path fill="#ddd" d="M12 21l-1.5-1.3C5 15 2 12.1 2 8.5 2 5.4 4.4 3 7.5 3c1.7 0 3.4.8 4.5 2.1C13.1 3.8 14.8 3 16.5 3 19.6 3 22 5.4 22 8.5c0 3.6-3 6.5-8.5 11.2z"/></svg>5 Hits</span>
    <span><svg width="11" height="10" viewBox="0 0 24 20"><ellipse cx="12" cy="9" rx="11" ry="8" fill="#ddd"/><path d="M4 14l-2 6 7-4z" fill="#ddd"/></svg>10 Comment</span>
  </div>
  <div class="body">
    <p>Fusce scelerisque augue a viverra semper. Etiam nisi nibh, vestibulum quis augue id, imperdiet fringilla dolor. Nulla sed nisl vel nisi cursus finibus. Vivamus ut augue nec justo viverra laoreet. Nunc efficitur, arcu ac cursus gravida, lorem elit commodo urna, id viverra libero tellus non ipsum. Fusce molestie ultrices nibh feugiat pretium. Donec pulvinar arcu metus, et dapibus odio condimentum id. Quisque malesuada mauris sit amet dui feugiat, ut pretium mauris luctus. Ut aliquam, tellus nec molestie condimentum, tellus arcu dignissim quam, a gravida nunc nulla vel magna. Sed pulvinar tortor et euismod blandit. Proin accumsan orci ac nunc fermentum vehicula.</p>
    <p>Cras quis neque urna. Pellentesque mollis, dui nec elementum elementum, ipsum quam suscipit ligula, sit amet lobortis dolor sem sed neque. Vivamus consequat est non sodales efficitur. Aliquam sodales eleifend sodales. Aliquam auctor ipsum quis nisl facilisis, at convallis mauris iaculis. Duis eleifend, magna ac convallis blandit, dui dui auctor leo, sed tincidunt nisi mauris ut nulla. Praesent porttitor dui ac turpis commodo porttitor. Integer ligula nisi, bibendum non sem at, porta condimentum dui.</p>
    <p>Proin id eleifend diam, euismod dictum nibh. Ut ullamcorper in purus at tempor. Nullam mattis risus nec velit semper lobortis. Donec accumsan ligula fermentum, ultricies massa eget, cursus leo. Suspendisse placerat elit et lacus aliquam, ut elementum leo aliquet. Integer ornare, ipsum eu lacinia viverra, lectus ipsum scelerisque nisl, nec iaculis leo elit id arcu. Aliquam id ante elit. Donec commodo purus eget lacus pharetra, et egestas metus blandit. Quisque pellentesque porta urna, sed dictum enim viverra a.</p>
  </div>
  <div class="gallery">
    <div class="g-leaf" role="img" aria-label="Single green cannabis leaf on a light green background"></div>
    <div class="g-buds" role="img" aria-label="Dried cannabis buds on a grey table"></div>
  </div>
  <div class="columns">
    <ol>
      <li>1. Donec ut metus sit amet elit consectetur facilisis id vel turpis.</li>
      <li>2. Aenean in mi eu elit mollis tincidunt.</li>
      <li>3. Etiam blandit metus vitae purus lacinia ultricies.</li>
      <li>4. Nunc quis nulla sagittis, faucibus neque a, tempus metus.</li>
      <li>5. In scelerisque libero ut mi ornare, a porttitor neque pulvinar.</li>
      <li>6. Morbi molestie lacus blandit interdum sodales.</li>
      <li>7. Curabitur eleifend velit molestie eleifend interdum.</li>
      <li>8. Vestibulum fringilla tortor et lorem sagittis,</li>
      <li>9. In scelerisque libero ut mi ornare, a porttitor neque pulvinar.</li>
      <li>10. Morbi molestie lacus blandit interdum sodales.</li>
      <li>11. Curabitur eleifend velit molestie eleifend interdum.</li>
    </ol>
    <div class="text">
      <p>Nulla quam turpis, commodo et placerat eu, mollis ut odio. Donec pellentesque egestas consequat. Vestibulum ante ipsum primis in faucibus orci luctus et ultrices posuere cubilia Curae; Nunc at urna dolor. Mauris odio nisi, rhoncus ac justo eget, lacinia iaculis lectus. Pellentesque id dapibus justo. Nunc venenatis non odio sed luctus. Etiam sit amet elit massa.</p>
      <p>Phasellus quis lorem eros. Aliquam non tincidunt nibh. Nulla quis interdum neque. Mauris volutpat neque eu nunc ornare ullamcorper. Sed neque velit, lobortis eget tellus in, pellentesque ornare nibh. Vestibulum ante ipsum primis in faucibus orci luctus et ultrices posuere cubilia Curae; Maecenas rutrum nisi non nibh egestas lacinia. Cras ut tellus sit amet lacus consequat dictum nec id sapien. Ut pellentesque ac ex ut elementum. Morbi mollis volutpat neque eu volutpat.</p>
      <p>Donec rhoncus massa quis nibh imperdiet dictum. Vestibulum id est sit amet felis fringilla bibendum at at leo. Proin molestie ac nisi eu laoreet. Integer faucibus enim nec ullamcorper tempor. Aenean nec felis dui. Integer tristique odio mi, in volutpat metus posuere eu. Aenean suscipit ipsum nunc, id volutpat lorem hendrerit ac. Sed id elit quam. In ac mauris arcu. Praesent eget lectus sit amet diam vestibulum varius. Suspendisse dignissim mattis leo, nec facilisis erat tempor quis. Vestibulum eu vestibulum ex. Maecenas luctus orci sed blandit fermentum. In vulputate eu metus a faucibus. Suspendisse feugiat condimentum congue.</p>
    </div>
  </div>

  <section class="comments">
    <article class="comment">
      <div class="avatar" role="img" aria-label="Commenter profile photo"></div>
      <div><h4>Dana Holt <small>( 12 January 2020 At 1:30AM )</small></h4>
      <p>Donec rhoncus massa quis nibh imperdiet dictum. Vestibulum id est sit amet felis fringilla bibendum at at leo. Proin molestie ac nisi eu laoreet. Integer faucibus enim nec ullamcorper tempor. Aenean nec felis dui. Integer tristique odio mi, in volutpat metus posuere eu. Aenean suscipit ipsum nunc, id volutpat lorem hendrerit ac. Sed id elit quam. In ac mauris arcu. Praesent eget lectus sit amet diam vestibulum varius. Suspendisse dignissim mattis leo, nec facilisis erat tempor quis. Vestibulum eu vestibulum ex.</p></div>
    </article>
    <article class="comment">
      <div class="avatar" role="img" aria-label="Commenter profile photo"></div>
      <div><h4>Dana Holt <small>( 12 January 2020 At 1:30AM )</small></h4>
      <p>Donec rhoncus massa quis nibh imperdiet dictum. Vestibulum id est sit amet felis fringilla bibendum at at leo. Proin molestie ac nisi eu laoreet. Integer faucibus enim nec ullamcorper tempor. Aenean nec felis dui. Integer tristique odio mi, in volutpat metus posuere eu. Aenean suscipit ipsum nunc, id volutpat lorem hendrerit ac. Sed id elit quam. In ac mauris arcu. Praesent eget lectus sit amet diam vestibulum varius. Suspendisse dignissim mattis leo, nec facilisis erat tempor quis. Vestibulum eu vestibulum ex.</p></div>
    </article>
    <article class="comment">
      <div class="avatar" role="img" aria-label="Commenter profile photo"></div>
      <div><h4>Dana Holt <small>( 12 January 2020 At 1:30AM )</small></h4>
      <p>Donec rhoncus massa quis nibh imperdiet dictum. Vestibulum id est sit amet felis fringilla bibendum at at leo. Proin molestie ac nisi eu laoreet. Integer faucibus enim nec ullamcorper tempor. Aenean nec felis dui. Integer tristique odio mi, in volutpat metus posuere eu. Aenean suscipit ipsum nunc, id volutpat lorem hendrerit ac. Sed id elit quam. In ac mauris arcu. Praesent eget lectus sit amet diam vestibulum varius. Suspendisse dignissim mattis leo, nec facilisis erat tempor quis. Vestibulum eu vestibulum ex.</p></div>
    </article>
  </section>

  <section class="leave">
    <h2>Leave your comment</h2>
    <div class="field"><label>Name</label><div class="box">Enter Your name</div></div>
    <div class="field"><label>Email</label><div class="box">Email</div></div>
    <div class="field"><label>Comment</label><div class="box area">Write Your Comment</div></div>
    <div class="btn">Post Comment</div>
  </section>
</main>

<footer class="footer">
  <div class="wrap cols">
    <div class="fcol about">
      <div class="brand">Harbor Velvet</div>
      Lorem ipsum dolor sit amet, consectetur adipiscing elit, sed do eiusmod tempor incididunt ut labore et.Lorem ipsum dolor sit amet, consectetur adipiscing
    </div>
    <div class="divider"></div>
    <div class="fcol news">
      <h3>Newsletter</h3>
      <div class="email">Enter your email</div>
      <div class="sub">SUBSCRIBE</div>
    </div>
    <div class="divider"></div>
    <div class="fcol store">
      <h3>Store Information</h3>
      Harbor Velvet Store, Demo store<br>USA 555-210<br>Call Us: 555-018-2746<br>Email Us: hello@harborvelvet.shop<br>Fax: 555019
    </div>
  </div>
  <div class="bottom">
    <div class="wrap">
      <span>© 2020 All Right Reserved</span>
      <div class="cards"><i></i><i></i><i></i><i></i><i></i></div>
    </div>
  </div>
</footer>

</body>
</html>
```